Furniture retail store requires in store display board design.

I am launching a new bed buying concept in my retail stores and require a point of sale graphic to explain the purchase process to consumers.
1.Select base style.(Including headboard) + 2. Customise legs and storage options. + 3.Choose Colours. + 4. Add your perfect mattress. = Your perfect nights sleep.
I'm imagining a sketchy/whiteboard/chalkboard type effect. The main boards will hang above a bed and will be 150cm wide x 35cm high.
Consumers 30yo+
Retail

```html
<!DOCTYPE html>
<html lang="en">
<head>
<meta charset="UTF-8">
<title>Bed Buying Steps – Display Board</title>
<link rel="stylesheet" href="https://fonts.googleapis.com/css2?family=Bebas+Neue&family=Kaushan+Script&display=swap">
<style>
  :root {
    --chalkboard: #1c1c1b;
    --chalkboard-light: #2c2c2a;
    --chalk-white: #f4f2ec;
    --chalk-yellow: #f3e21c;
    --photo-wall: #d9ccb0;
    --photo-light: #efe7d6;
    --photo-bed: #cfc8b8;
    --photo-shadow: #8d7d62;
  }
  html, body {
    margin: 0;
    padding: 0;
    overflow: hidden;
    background: #ffffff;
  }
  .board {
    position: relative;
    width: 1200px;
    height: 280px;
    overflow: hidden;
    background:
      radial-gradient(ellipse at 30% 40%, var(--chalkboard-light) 0%, var(--chalkboard) 70%);
  }
  .steps {
    position: absolute;
    left: 22px;
    top: 30px;
    margin: 0;
    padding: 0;
    list-style: none;
    font-family: "Bebas Neue", "Arial Narrow", sans-serif;
    font-size: 37px;
    line-height: 51px;
    color: var(--chalk-white);
    letter-spacing: 0.2px;
    transform: scaleX(0.9);
    transform-origin: left top;
  }
  .equals {
    position: absolute;
    left: 444px;
    top: 166px;
    width: 54px;
    height: 34px;
  }
  .equals span {
    position: absolute;
    left: 0;
    width: 54px;
    height: 9px;
    background: var(--chalk-yellow);
    border-radius: 2px;
  }
  .equals span:first-child { top: 2px; }
  .equals span:last-child { top: 22px; }
  .tagline {
    position: absolute;
    left: 515px;
    top: 52px;
    margin: 0;
    font-family: "Kaushan Script", cursive;
    font-weight: 400;
    font-size: 62px;
    line-height: 72px;
    color: var(--chalk-yellow);
    transform: rotate(-9deg);
    transform-origin: left top;
  }
  .tagline .line-two {
    display: block;
    padding-left: 14px;
  }
  .bedroom-photo {
    position: absolute;
    left: 862px;
    top: 0;
    width: 338px;
    height: 280px;
    background:
      linear-gradient(180deg, var(--photo-light) 0%, var(--photo-wall) 45%, var(--photo-bed) 60%, var(--photo-shadow) 100%);
  }
</style>
</head>
<body>
  <div class="board">
    <ol class="steps">
      <li>1. Select base style (includingheadboard) +</li>
      <li>2. Customise legs and storage options +</li>
      <li>3. Choose colours +</li>
      <li>4.&nbsp; Add your perfect mattress</li>
    </ol>
    <div class="equals" aria-hidden="true"><span></span><span></span></div>
    <p class="tagline">Your Perfect<span class="line-two">Nights Sleep</span></p>
    <div class="bedroom-photo" role="img" aria-label="Photograph of a made-up bed with white pillows and linen in a softly lit bedroom with a framed artwork and bedside lamp"></div>
  </div>
</body>
</html>
```